Self-Help & Training Association Business Card Design Project

We need double-sided business card for our Self-Help and Training Association called "Crescitalba".

We want Pibo.com to print them, both Velta and Standard Business Card format (**PLEASE DON'T SUBMIT ROUNDED-CORNERS CARDS).

(more info: http://uk.pibo-print.example)

We ask designers to submit project based on our logo (attached) and color-set and to do it according to Pibo.com designing guidelines.

We will print three variations (for three people) of the business card.

Let's apply now!

Thank you!

Target Market(s)

Common people

Industry/Entity Type

Business

Requirements
Must have
• Strings needed:

Association Name: Crescitalba
Tagline: Formarsi per Vivere Meglio
Web: www.crescitalba.example

Person Name: Luca Ferrandi
Person Title: Direttore Scientifico e Lead Trainer
Mobile: (+39) 347 5081934
E-mail: luca@crescitalba.example

Could be a nice idea to put general details on the front and personal details on the back of the card.

-
Artwork guidelines
You can use PIBO's online tools to position and crop your images, but if you'd like to pre-design your Business Cards, before you upload these are the dimensions you need:

Full bleed size
(Recommended for creating artwork - this includes the bleed, which will be cropped in production. Please note, you do not need to add crop marks to your artwork)

1039 x 697 pixels (300dpi)
88mm x 59mm (300dpi)
3.46" x 2.32" (300dpi)
Final size when trimmed
84mm x 55mm
3.30" x 2.16"
Accepted file types
We accept high resolution GIFs, PNGs, PDFs, and JPGs.

-

See http://www.crescitalba.example/ for colors and style reference.

Thank you!
Nice to have
• If you still have empty space, this quote will be cool to be added:

"Non è il più forte o il più intelligente a sopravvivere, ma chi si adatta più velocemente al cambiamento. (G. Pellow)"

```html
<!DOCTYPE html>
<html lang="it">
<head>
<meta charset="utf-8">
<title>Crescitalba – Biglietto da visita</title>
<link rel="stylesheet" href="https://fonts.googleapis.com/css2?family=Didact+Gothic&family=Righteous&display=swap">
<style>
  :root {
    --teal: #4fb3ad;
    --teal-soft: #9fd8d3;
    --teal-pale: #d9f1ee;
    --teal-deep: #2a8f8a;
    --ink: #141414;
    --paper: #ffffff;
  }
  * { margin: 0; padding: 0; box-sizing: border-box; }
  html, body { width: 1200px; height: 334px; overflow: hidden; background: var(--paper); }
  body { position: relative; font-family: "Didact Gothic", sans-serif; color: var(--ink); }

  .card {
    position: absolute;
    top: 7px;
    width: 588px;
    height: 322px;
    overflow: hidden;
    background: linear-gradient(180deg, var(--paper) 0%, var(--paper) 38%, var(--teal-pale) 62%, var(--teal-soft) 88%, var(--teal) 100%);
  }
  .card--front { left: 8px; }
  .card--back { left: 606px; }

  .floral {
    position: absolute;
    pointer-events: none;
  }
  .floral--side-left {
    left: 0; top: 40px; width: 90px; height: 240px;
    background: radial-gradient(ellipse at 20% 50%, rgba(79,179,173,0.45), rgba(79,179,173,0) 70%);
  }
  .floral--corner-right {
    right: 0; top: 0; width: 150px; height: 260px;
    background: radial-gradient(ellipse at 85% 35%, rgba(79,179,173,0.5), rgba(79,179,173,0) 70%);
  }
  .floral--bottom {
    left: 0; bottom: 0; width: 100%; height: 70px;
    background: linear-gradient(180deg, rgba(255,255,255,0) 0%, rgba(255,255,255,0.35) 60%, rgba(255,255,255,0.15) 100%);
  }

  .brand {
    position: absolute;
    top: 12px; left: 14px;
    display: flex; align-items: center; gap: 10px;
  }
  .brand__mark {
    width: 30px; height: 30px;
    background: var(--teal);
  }
  .brand__name {
    font-size: 13px;
    font-weight: 400;
    letter-spacing: 0.3px;
    color: var(--ink);
  }

  .web {
    position: absolute;
    top: 22px; right: 38px;
    font-size: 10px;
    color: var(--ink);
  }

  .front__title {
    position: absolute;
    top: 96px; left: 0; width: 100%;
    text-align: center;
    font-family: "Righteous", sans-serif;
    font-size: 32px;
    letter-spacing: 2px;
    color: var(--teal);
  }
  .front__tagline {
    position: absolute;
    top: 144px; left: 0; width: 100%;
    text-align: center;
    font-size: 17px;
    color: var(--teal-deep);
  }
  .front__quote {
    position: absolute;
    top: 250px; left: 0; width: 100%;
    text-align: center;
    font-size: 14px;
    line-height: 19px;
    color: var(--ink);
  }

  .person__name {
    position: absolute;
    top: 74px; left: 0; width: 100%;
    text-align: center;
    font-family: "Righteous", sans-serif;
    font-size: 22px;
    letter-spacing: 1.5px;
    color: var(--teal);
  }
  .person__role {
    position: absolute;
    top: 108px; left: 0; width: 100%;
    text-align: center;
    font-size: 16px;
    color: var(--ink);
  }
  .contact {
    position: absolute;
    top: 190px; left: 178px;
    list-style: none;
    font-size: 14px;
    line-height: 21px;
    color: var(--ink);
  }
</style>
</head>
<body>
  <section class="card card--front" aria-label="Fronte del biglietto">
    <div class="floral floral--side-left" role="img" aria-label="Decorazione floreale a volute turchese"></div>
    <div class="floral floral--corner-right" role="img" aria-label="Decorazione floreale a volute turchese"></div>
    <div class="floral floral--bottom" role="img" aria-label="Fascia di fiori e volute chiare"></div>

    <div class="brand">
      <span class="brand__mark"></span>
      <span class="brand__name">CRESCITALBA</span>
    </div>
    <p class="web">www.crescitalba.example</p>

    <h1 class="front__title">CRESCITALBA</h1>
    <p class="front__tagline">Formarsi per Vivere Meglio</p>
    <p class="front__quote">Non è il più forte o il più intelligente a sopravvivere,<br>ma chi si adatta più velocemente al cambiamento. (G. Pellow)</p>
  </section>

  <section class="card card--back" aria-label="Retro del biglietto">
    <div class="floral floral--side-left" role="img" aria-label="Decorazione floreale a volute turchese"></div>
    <div class="floral floral--corner-right" role="img" aria-label="Decorazione floreale a volute turchese"></div>
    <div class="floral floral--bottom" role="img" aria-label="Fascia di fiori e volute chiare"></div>

    <div class="brand">
      <span class="brand__mark"></span>
      <span class="brand__name">CRESCITALBA</span>
    </div>

    <h2 class="person__name">LUCA FERRANDI</h2>
    <p class="person__role">Direttore Scientifico e Lead Trainer</p>
    <ul class="contact">
      <li>Mobile:&nbsp; (+39) 347 5081934</li>
      <li>E-mail: luca@crescitalba.example</li>
    </ul>
  </section>
</body>
</html>
```